Our desktop web app builder needs a redesign

We want to redesign our low-code web app builder called Fernhold. Fernhold runs in desktop environments and is aimed at IT professionals and developers.

The UI consists of a button bar, multiple panels and a tabbed working area. We are looking to completely change the look and feel of the application interfaces, while keeping the layout and functionality the same.

We would like to see your ideas for fonts, sizing, colour, icons and any other visual UI element. Your work can be a rough mockup of your design ideas, and does not need to be pixel perfect. Legibility and optimised use of space are key.

More details about the app and how it works here: https://fernhold.software/

If we like your ideas, we will get in touch with you and work with you to develop the new design in greater detail.

```html
<!DOCTYPE html>
<html lang="en">
<head>
<meta charset="utf-8">
<title>Fernhold Designer</title>
<link href="https://fonts.googleapis.com/css2?family=Mulish:wght@400;500;600;700&display=swap" rel="stylesheet">
<style>
:root{
  --brand:#0bb4d6;
  --brand-soft:#a6e6f1;
  --brand-pale:#c9eef5;
  --bar:#f2f3f5;
  --panel:#f0f1f3;
  --canvas:#f7f8fa;
  --ink:#3d4148;
  --ink-soft:#6b7079;
  --muted:#b9bdc3;
  --line:#d6d9dd;
  --danger:#e8453c;
  --white:#ffffff;
}
*{box-sizing:border-box;margin:0;padding:0}
html,body{width:1200px;height:868px;overflow:hidden}
body{font-family:"Mulish",sans-serif;color:var(--ink);background:var(--white);position:relative;font-size:12px}
.abs{position:absolute}
svg{display:block}

/* title bar */
.titlebar{left:0;top:0;width:1200px;height:32px;background:var(--brand);color:var(--white)}
.menu{left:12px;top:0;height:32px;display:flex;gap:17px;align-items:center;font-size:13px}
.app-title{left:0;width:1200px;top:0;height:32px;line-height:32px;text-align:center;font-weight:700;font-size:14px}
.win-ctrl{right:12px;top:9px;display:flex;gap:12px}

/* toolbar */
.toolbar{left:0;top:32px;width:1200px;height:70px;background:var(--bar)}
.brand{left:25px;top:52px;display:flex;align-items:center;gap:9px;color:var(--brand);font-size:24px;font-weight:500;letter-spacing:1px}
.brand-dot{width:22px;height:22px;border-radius:50%;border:3px solid var(--brand)}
.tool{top:46px;width:70px;margin-left:-35px;text-align:center;font-size:11.5px;color:var(--ink-soft)}
.tool svg{margin:0 auto 4px;width:20px;height:20px}
.tool.off{color:var(--ink-soft)}
.sep{top:42px;width:1px;height:48px;background:var(--line)}

/* tabs */
.tab{top:107px;height:30px;line-height:28px;text-align:center;font-size:12px;border:1px solid var(--line);background:var(--bar);color:var(--ink-soft)}
.tab.active{background:var(--brand-soft);border-color:var(--brand-soft);color:var(--ink)}
.tab-add{left:459px;top:115px;width:15px;height:15px;border-radius:50%;background:var(--brand);color:var(--white);font-weight:700;font-size:14px;line-height:15px;text-align:center}

/* panels */
.panel{background:var(--panel)}
.panel-head{height:30px;border-bottom:2px solid var(--brand)}
.panel-tab{position:absolute;left:0;top:0;height:30px;line-height:30px;padding:0 13px;background:var(--brand);color:var(--white);font-size:13px}
.panel-icons{position:absolute;right:8px;top:8px;display:flex;gap:8px}

.tree-row{left:0;width:201px;height:19px;line-height:19px;font-size:12px}
.tree-row.sel{background:var(--brand-soft)}
.caret{position:absolute;top:6px}

.val-head{left:34px;top:620px;font-weight:600;font-size:12px}
.val-row{left:13px;display:flex;gap:10px;align-items:center;font-size:12px;color:var(--ink-soft)}

.work{left:206px;top:135px;width:719px;height:733px;background:var(--canvas)}
.vscroll{background:var(--brand);border-radius:1px}

/* toolbox */
.section{left:962px;top:174px;font-size:13px;color:var(--ink-soft)}
.section-line{left:955px;top:194px;width:210px;height:2px;background:var(--brand)}
.cell{width:66px;height:58px;border:1px solid var(--line);background:var(--bar);text-align:center;font-size:11px;color:var(--ink-soft);line-height:1.05}
.cell svg{margin:10px auto 4px;width:18px;height:18px}
.cell.hot{background:var(--brand-soft);border-color:var(--brand-soft)}

/* properties */
.prop-label{left:948px;font-size:11.5px;color:var(--ink-soft)}
.prop-group{left:948px;font-size:11.5px;font-weight:700;color:var(--ink)}
.prop-line{left:948px;width:222px;height:1px;background:var(--brand)}
.field{background:var(--brand-soft);font-size:11.5px;color:var(--ink-soft);padding-left:8px;line-height:19px;height:19px}
.check{width:13px;height:13px;background:var(--brand-soft)}
</style>
</head>
<body>

<!-- title bar -->
<div class="abs titlebar"></div>
<div class="abs app-title">Fernhold Designer</div>
<nav class="abs menu" style="color:#fff"><span>File</span><span>Edit</span><span>Insert</span><span>Run</span><span>Window</span><span>Help</span></nav>
<div class="abs win-ctrl">
  <svg width="12" height="12" viewBox="0 0 12 12"><path d="M1 10h10" stroke="#fff" stroke-width="2"/></svg>
  <svg width="12" height="12" viewBox="0 0 12 12"><rect x="1.5" y="1.5" width="9" height="9" fill="none" stroke="#fff" stroke-width="2"/></svg>
  <svg width="12" height="12" viewBox="0 0 12 12"><path d="M1 1l10 10M11 1L1 11" stroke="#fff" stroke-width="2.4"/></svg>
</div>

<!-- toolbar -->
<div class="abs toolbar"></div>
<div class="abs brand"><span class="brand-dot"></span>FERNHOLD</div>

<div class="abs tool" style="left:242px"><svg viewBox="0 0 20 20"><path d="M2 5h6l2 2h8v10H2z" fill="#0bb4d6"/></svg>Open</div>
<div class="abs tool" style="left:288px"><svg viewBox="0 0 20 20"><path d="M3 3h12l2 2v12H3z" fill="#b9bdc3"/><rect x="6" y="4" width="7" height="4" fill="#f2f3f5"/></svg>Save</div>
<div class="abs sep" style="left:327px"></div>
<div class="abs tool" style="left:369px"><svg viewBox="0 0 20 20"><path d="M4 2h8l4 4v12H4z" fill="#4a4e55"/><path d="M7 10h6M7 13h6" stroke="#f2f3f5" stroke-width="1.5"/></svg>Page</div>
<div class="abs tool" style="left:417px"><svg viewBox="0 0 20 20"><rect x="4" y="3" width="12" height="15" fill="none" stroke="#4a4e55" stroke-width="2"/><path d="M7 7h6M7 10h6M7 13h6" stroke="#4a4e55" stroke-width="1.5"/></svg>Script</div>
<div class="abs tool" style="left:464px"><svg viewBox="0 0 20 20"><rect x="4" y="2" width="12" height="16" fill="#b9bdc3"/><path d="M7 7h6M7 10h6M7 13h6" stroke="#f2f3f5" stroke-width="1.5"/></svg>Type</div>
<div class="abs tool" style="left:520px"><svg viewBox="0 0 20 20"><rect x="3" y="3" width="14" height="14" fill="none" stroke="#4a4e55" stroke-width="2"/><path d="M3 8h14M9 8v9" stroke="#4a4e55" stroke-width="2"/></svg>Template</div>
<div class="abs tool" style="left:579px"><svg viewBox="0 0 20 20"><path d="M2 5h6l2 2h8v10H2z" fill="#c6c9ce"/></svg>Folder</div>
<div class="abs tool" style="left:641px"><svg viewBox="0 0 20 20"><path d="M4 8h12l-3-3M16 12H4l3 3" fill="none" stroke="#c6c9ce" stroke-width="2"/></svg>Connector</div>
<div class="abs sep" style="left:694px"></div>
<div class="abs tool" style="left:776px"><svg viewBox="0 0 20 20"><rect x="3" y="3" width="14" height="14" fill="none" stroke="#c6c9ce" stroke-width="2"/><path d="M6 7h8M6 10h8M6 13h8" stroke="#c6c9ce" stroke-width="1.5"/></svg>Create Form</div>
<div class="abs tool" style="left:848px"><svg viewBox="0 0 20 20"><rect x="2" y="3" width="16" height="14" rx="2" fill="#4a4e55"/><ellipse cx="10" cy="11" rx="5" ry="3" fill="#f2f3f5"/><circle cx="10" cy="11" r="1.5" fill="#4a4e55"/></svg>Preview</div>
<div class="abs tool" style="left:907px"><svg viewBox="0 0 20 20"><path d="M5 9v9h10V9M10 13V2M6 6l4-4 4 4" fill="none" stroke="#4a4e55" stroke-width="2"/></svg>Publish</div>
<div class="abs sep" style="left:976px"></div>
<div class="abs tool" style="left:1032px"><svg viewBox="0 0 20 20"><path d="M2 2h16v12H8l-4 4v-4H2z" fill="#e8453c"/><path d="M10 5v5M10 11.5v1.5" stroke="#fff" stroke-width="2"/></svg>Feedback</div>
<div class="abs tool" style="left:1101px"><svg viewBox="0 0 20 20"><path d="M1 8l9-4 9 4-9 4z" fill="#c6c9ce"/><path d="M5 10v4c3 2 7 2 10 0v-4l-5 2z" fill="#c6c9ce"/></svg>Academy</div>
<div class="abs tool" style="left:1151px"><svg viewBox="0 0 20 20"><circle cx="10" cy="10" r="9" fill="#0bb4d6"/><path d="M7.5 8a2.5 2.5 0 1 1 3.5 2.3c-.8.4-1 1-1 1.7M10 14v1.5" fill="none" stroke="#fff" stroke-width="2"/></svg>Help</div>

<!-- tabs -->
<div class="abs tab active" style="left:210px;width:77px">View Bug</div>
<div class="abs tab" style="left:293px;width:77px">Add Bug</div>
<div class="abs tab" style="left:377px;width:76px">Home</div>
<div class="abs tab-add">+</div>

<!-- application explorer -->
<section class="abs panel" style="left:0;top:135px;width:201px;height:425px">
  <div class="panel-head" style="position:relative"><span class="panel-tab" style="width:142px">Application Explorer</span>
    <span class="panel-icons">
      <svg width="13" height="13" viewBox="0 0 13 13"><path d="M5 2H2v9h9V8M7 1h5v5M12 1L6 7" fill="none" stroke="#0bb4d6" stroke-width="1.5"/></svg>
      <svg width="13" height="13" viewBox="0 0 13 13"><path d="M2 2l9 9M11 2l-9 9" stroke="#0bb4d6" stroke-width="2.4"/></svg>
    </span>
  </div>
</section>
<div class="abs tree-row" style="top:168px;padding-left:34px;font-weight:600"><svg class="caret" style="left:13px" width="8" height="6" viewBox="0 0 8 6"><path d="M0 0h8L4 6z" fill="#0bb4d6"/></svg>Bugbear</div>
<div class="abs tree-row" style="top:189px;padding-left:50px"><svg class="caret" style="left:37px;top:5px" width="5" height="8" viewBox="0 0 5 8"><path d="M0 0l5 4-5 4z" fill="#0bb4d6"/></svg>Pages</div>
<div class="abs tree-row" style="top:209px;padding-left:66px"><svg class="caret" style="left:51px" width="8" height="6" viewBox="0 0 8 6"><path d="M0 0h8L4 6z" fill="#0bb4d6"/></svg>Tickly</div>
<div class="abs tree-row" style="top:229px;padding-left:66px"><svg class="caret" style="left:51px" width="8" height="6" viewBox="0 0 8 6"><path d="M0 0h8L4 6z" fill="#0bb4d6"/></svg>Add Bug</div>
<div class="abs tree-row" style="top:247px;padding-left:66px"><svg class="caret" style="left:51px" width="8" height="6" viewBox="0 0 8 6"><path d="M0 0h8L4 6z" fill="#0bb4d6"/></svg>Home</div>
<div class="abs tree-row sel" style="top:266px;padding-left:66px;font-weight:600"><svg class="caret" style="left:51px" width="8" height="6" viewBox="0 0 8 6"><path d="M0 0h8L4 6z" fill="#0bb4d6"/></svg>View Bug</div>
<div class="abs tree-row" style="top:285px;padding-left:50px">Types</div>
<div class="abs tree-row" style="top:305px;padding-left:50px"><svg class="caret" style="left:37px;top:5px" width="5" height="8" viewBox="0 0 5 8"><path d="M0 0l5 4-5 4z" fill="#0bb4d6"/></svg>Templates</div>
<div class="abs tree-row" style="top:326px;padding-left:50px">Styles</div>
<div class="abs tree-row" style="top:346px;padding-left:50px">Settings</div>
<div class="abs tree-row" style="top:367px;padding-left:50px"><svg class="caret" style="left:37px;top:5px" width="5" height="8" viewBox="0 0 5 8"><path d="M0 0l5 4-5 4z" fill="#0bb4d6"/></svg>Embedded Files</div>
<div class="abs tree-row" style="top:387px;padding-left:50px"><svg class="caret" style="left:37px;top:5px" width="5" height="8" viewBox="0 0 5 8"><path d="M0 0l5 4-5 4z" fill="#0bb4d6"/></svg>Connectors</div>

<!-- validations -->
<section class="abs panel" style="left:0;top:567px;width:201px;height:301px">
  <div class="panel-head" style="position:relative"><span class="panel-tab" style="width:92px">Validations</span>
    <span class="panel-icons">
      <svg width="13" height="13" viewBox="0 0 13 13"><path d="M5 2H2v9h9V8M7 1h5v5M12 1L6 7" fill="none" stroke="#0bb4d6" stroke-width="1.5"/></svg>
      <svg width="13" height="13" viewBox="0 0 13 13"><path d="M2 2l9 9M11 2l-9 9" stroke="#0bb4d6" stroke-width="2.4"/></svg>
    </span>
  </div>
</section>
<div class="abs val-head">Descriptions</div>
<div class="abs val-row" style="top:645px"><svg width="12" height="12" viewBox="0 0 12 12"><path d="M1 1l10 10M11 1L1 11" stroke="#e8453c" stroke-width="2.6"/></svg>No page has been linked...</div>
<div class="abs val-row" style="top:670px"><svg width="12" height="12" viewBox="0 0 12 12"><path d="M1 1l10 10M11 1L1 11" stroke="#e8453c" stroke-width="2.6"/></svg>No page has been linked...</div>
<div class="abs val-row" style="top:695px"><svg width="12" height="12" viewBox="0 0 12 12"><path d="M1 1l10 10M11 1L1 11" stroke="#e8453c" stroke-width="2.6"/></svg>No page has been linked...</div>
<div class="abs val-row" style="top:721px"><svg width="12" height="12" viewBox="0 0 12 12"><path d="M1 1l10 10M11 1L1 11" stroke="#e8453c" stroke-width="2.6"/></svg>No page has been linked...</div>
<div class="abs val-row" style="top:746px"><svg width="12" height="12" viewBox="0 0 12 12"><path d="M1 1l10 10M11 1L1 11" stroke="#e8453c" stroke-width="2.6"/></svg>No page has been linked...</div>

<!-- working area -->
<main class="abs work"></main>
<div class="abs vscroll" style="left:927px;top:135px;width:8px;height:733px;background:var(--brand-pale)"></div>
<div class="abs vscroll" style="left:927px;top:135px;width:8px;height:10px"></div>
<div class="abs vscroll" style="left:927px;top:150px;width:8px;height:236px"></div>
<div class="abs vscroll" style="left:927px;top:852px;width:8px;height:10px"></div>

<!-- toolbox -->
<section class="abs panel" style="left:940px;top:135px;width:252px;height:465px;background:#fff">
  <div class="panel-head" style="position:relative"><span class="panel-tab" style="width:74px">Toolbox</span>
    <span class="panel-icons">
      <svg width="13" height="13" viewBox="0 0 13 13"><path d="M5 2H2v9h9V8M7 1h5v5M12 1L6 7" fill="none" stroke="#0bb4d6" stroke-width="1.5"/></svg>
      <svg width="13" height="13" viewBox="0 0 13 13"><path d="M2 2l9 9M11 2l-9 9" stroke="#0bb4d6" stroke-width="2.4"/></svg>
    </span>
  </div>
</section>
<div class="abs section">View</div>
<div class="abs section-line"></div>
<div class="abs vscroll" style="left:1182px;top:196px;width:8px;height:402px;background:var(--brand-pale)"></div>
<div class="abs vscroll" style="left:1182px;top:210px;width:8px;height:375px"></div>

<div class="abs cell hot" style="left:955px;top:202px"><svg viewBox="0 0 18 18"><circle cx="9" cy="9" r="8" fill="none" stroke="#3d4148" stroke-width="1.8"/><circle cx="9" cy="9" r="4.5" fill="#3d4148"/></svg>Button</div>
<div class="abs cell" style="left:1027px;top:202px"><svg viewBox="0 0 18 18"><path d="M2 2v14h14M6 13V9M9 13V7M12 13V10" fill="none" stroke="#3d4148" stroke-width="1.8"/></svg>Chart</div>
<div class="abs cell" style="left:1099px;top:202px"><svg viewBox="0 0 18 18"><rect x="2" y="3" width="14" height="13" fill="none" stroke="#3d4148" stroke-width="1.8"/><path d="M5 9l3 3 5-6" fill="none" stroke="#3d4148" stroke-width="1.8"/></svg>Check Box</div>

<div class="abs cell" style="left:955px;top:267px"><svg style="margin-top:9px;margin-bottom:2px" viewBox="0 0 18 18"><rect x="1" y="1" width="16" height="16" fill="#3d4148"/><path d="M4 6h5M4 10h5M10 11l2 2 3-5" fill="none" stroke="#fff" stroke-width="1.5"/></svg>Check Box<br>List</div>
<div class="abs cell" style="left:1027px;top:267px"><svg viewBox="0 0 18 18"><rect x="2" y="3" width="14" height="12" fill="none" stroke="#3d4148" stroke-width="1.8"/><path d="M2 7h14M2 11h14M7 3v12M11 3v12" stroke="#3d4148" stroke-width="1.4"/></svg>Data Grid</div>
<div class="abs cell" style="left:1099px;top:267px"><svg viewBox="0 0 18 18"><rect x="2" y="2" width="6" height="6" fill="#3d4148"/><rect x="2" y="10" width="6" height="6" fill="#3d4148"/><path d="M10 5h5v5M15 13h-5" fill="none" stroke="#3d4148" stroke-width="1.8"/></svg>Date Picker</div>

<div class="abs cell" style="left:955px;top:333px"><svg viewBox="0 0 18 18"><rect x="1" y="5" width="16" height="8" fill="none" stroke="#3d4148" stroke-width="1.6"/><path d="M11 5v8M12.5 8l1.5 2 1.5-2" fill="none" stroke="#3d4148" stroke-width="1.3"/></svg>Drop Down</div>
<div class="abs cell" style="left:1027px;top:333px"><svg viewBox="0 0 18 18"><rect x="2" y="2" width="14" height="14" fill="none" stroke="#3d4148" stroke-width="1.8"/><path d="M3 14l4-5 3 3 2-2 3 4" fill="none" stroke="#3d4148" stroke-width="1.6"/></svg>Image</div>
<div class="abs cell" style="left:1099px;top:333px"><svg viewBox="0 0 18 18"><path d="M1 3h9M5.5 3v12M9 8h8M13 8v7" stroke="#3d4148" stroke-width="2"/></svg>Label</div>

<div class="abs cell" style="left:955px;top:398px"><svg viewBox="0 0 18 18"><rect x="1" y="5" width="9" height="8" rx="4" fill="none" stroke="#3d4148" stroke-width="1.8"/><rect x="8" y="5" width="9" height="8" rx="4" fill="none" stroke="#3d4148" stroke-width="1.8"/></svg>Link</div>
<div class="abs cell" style="left:1027px;top:398px"><svg viewBox="0 0 18 18"><path d="M2 4h14M2 9h14M2 14h14" stroke="#3d4148" stroke-width="1.8"/></svg>Menu</div>
<div class="abs cell" style="left:1099px;top:398px"><svg viewBox="0 0 18 18"><rect x="2" y="4" width="14" height="10" fill="none" stroke="#3d4148" stroke-width="1.6"/></svg>Panel</div>

<div class="abs cell" style="left:955px;top:465px"><svg style="margin-top:8px;margin-bottom:2px" viewBox="0 0 18 18"><rect x="2" y="1" width="14" height="16" fill="none" stroke="#3d4148" stroke-width="1.6"/><path d="M5 5h1M8 5h5M5 9h1M8 9h5M5 13h1M8 13h5" stroke="#3d4148" stroke-width="1.6"/></svg>Radio<br>Button L..</div>
<div class="abs cell" style="left:1027px;top:465px"><svg viewBox="0 0 18 18"><path d="M3 8a6 5 0 0 1 11-2M15 10a6 5 0 0 1-11 2M14 2v4h-4M4 16v-4h4" fill="none" stroke="#3d4148" stroke-width="1.7"/></svg>Repeater</div>
<div class="abs cell" style="left:1099px;top:465px"><svg viewBox="0 0 18 18"><rect x="2" y="2" width="14" height="14" fill="none" stroke="#3d4148" stroke-width="1.6"/><path d="M6 13l3-8 3 8M7 10h4" fill="none" stroke="#3d4148" stroke-width="1.5"/></svg>Text Box</div>

<div class="abs cell" style="left:955px;top:531px"><svg viewBox="0 0 18 18"><path d="M4 14a4 4 0 0 1 0-8 5 5 0 0 1 10 1 3.5 3.5 0 0 1 0 7z" fill="#3d4148"/><path d="M9 13V8M7 10l2-2 2 2" fill="none" stroke="#fff" stroke-width="1.5"/></svg>Upload</div>

<!-- properties -->
<section class="abs panel" style="left:940px;top:608px;width:252px;height:260px;background:#fff">
  <div class="panel-head" style="position:relative"><span class="panel-tab" style="width:145px">Properties (DataG...)</span>
    <span class="panel-icons">
      <svg width="13" height="13" viewBox="0 0 13 13"><path d="M5 2H2v9h9V8M7 1h5v5M12 1L6 7" fill="none" stroke="#0bb4d6" stroke-width="1.5"/></svg>
      <svg width="13" height="13" viewBox="0 0 13 13"><path d="M2 2l9 9M11 2l-9 9" stroke="#0bb4d6" stroke-width="2.4"/></svg>
    </span>
  </div>
</section>
<div class="abs prop-group" style="top:656px">Name</div>
<div class="abs field" style="left:1050px;top:654px;width:132px">HistoryDataGrid</div>
<div class="abs prop-line" style="top:681px"></div>
<div class="abs prop-group" style="top:691px">Data</div>
<div class="abs prop-label" style="top:712px">Columns</div>
<div class="abs field" style="left:1050px;top:710px;width:111px">(Collection)</div>
<svg class="abs" style="left:1163px;top:712px" width="15" height="14" viewBox="0 0 15 14"><rect x="1" y="1" width="13" height="12" fill="none" stroke="#0bb4d6" stroke-width="1.6"/><path d="M7.5 1v12" stroke="#0bb4d6" stroke-width="1.6"/></svg>
<div class="abs prop-line" style="top:737px"></div>
<div class="abs prop-group" style="top:745px">Optional</div>
<div class="abs prop-label" style="top:766px">Allow Export</div>
<div class="abs check" style="left:1060px;top:767px"></div>
<div class="abs prop-label" style="top:789px">Display Search Bar</div>
<div class="abs check" style="left:1060px;top:790px"></div>
<div class="abs prop-label" style="top:811px">Selectable Data</div>
<div class="abs check" style="left:1060px;top:812px"></div>
<div class="abs prop-label" style="top:834px">Selectable Data</div>
<div class="abs field" style="left:1060px;top:834px;width:122px;height:16px;line-height:16px">true</div>
<svg class="abs" style="left:1168px;top:835px" width="14" height="14" viewBox="0 0 14 14"><rect x="1" y="1" width="12" height="12" fill="#fff" stroke="#0bb4d6" stroke-width="1.5"/><path d="M4 5.5l3 3 3-3" fill="none" stroke="#0bb4d6" stroke-width="1.6"/></svg>

</body>
</html>
```